Browse Every Counter Midtown Harlanby Event

We are hosting a Browse Every Counter Midtown Harlanby event in conjunction with Corvella Charge's Corner Trader Festday. Participants will be given a passport to get stamped at participating businesses. They will be entered to win $$ prizes! I have attached a Word document with the info that needs to be included.

Target Market(s)

Christmas shoppers, mainly women.

Colors
f04a50
31b7a3

Requirements
Must have
• The info attached. Christmas or holiday images.

```html
<!DOCTYPE html>
<html lang="en">
<head>
<meta charset="utf-8">
<title>Browse Every Counter Midtown Harlanby – Flyer</title>
<link href="https://fonts.googleapis.com/css2?family=Barlow+Condensed:wght@500;600;700&family=Great+Vibes&family=Open+Sans:wght@600;700&family=Roboto+Condensed:wght@400;500&display=swap" rel="stylesheet">
<style>
  :root{
    --backdrop:#0f2447;
    --paper:#ffffff;
    --pine:#1d7a3a;
    --pine-dark:#155e2c;
    --berry:#d9142a;
    --berry-dark:#b30f22;
    --ink:#111111;
    --brand-blue:#1f5fae;
  }
  *{box-sizing:border-box;margin:0;padding:0}
  html,body{width:1200px;height:1000px;overflow:hidden;background:var(--backdrop)}
  .flyer{position:absolute;left:296px;top:70px;width:616px;height:870px;background:var(--paper);overflow:hidden;font-family:"Roboto Condensed",sans-serif}
  .flyer-art{position:absolute;left:0;top:0;width:616px;height:870px}
  .line{position:absolute;left:0;right:0;text-align:center;line-height:1;white-space:nowrap}
  .brand-host{position:absolute;left:128px;top:36px;color:var(--pine);font-family:"Barlow Condensed",sans-serif;font-weight:600;font-size:28px;letter-spacing:1px}
  .brand-partner{position:absolute;left:364px;top:30px;display:flex;align-items:center;gap:8px;color:var(--brand-blue);font-family:"Barlow Condensed",sans-serif;font-weight:600;font-size:17px;line-height:1.05}
  .brand-partner .dot{width:40px;height:40px;border-radius:50%;background:var(--brand-blue);flex:none}
  .title-script{top:290px;font-family:"Great Vibes",cursive;font-size:56px;color:#fff}
  .title-place{top:352px;font-family:"Barlow Condensed",sans-serif;font-weight:600;font-size:42px;color:#fff;letter-spacing:.5px}
  .date-pill{position:absolute;left:102px;top:408px;width:410px;height:44px;border-radius:22px;background:linear-gradient(var(--berry),var(--berry-dark));color:#fff;font-family:"Barlow Condensed",sans-serif;font-weight:600;font-size:23px;display:flex;align-items:center;justify-content:center}
  .prize-main{top:466px;color:var(--pine);font-family:"Barlow Condensed",sans-serif;font-weight:700;font-size:25px}
  .prize-sub{top:495px;font-size:16px;color:var(--ink)}
  .santa{top:545px;color:var(--berry);font-family:"Barlow Condensed",sans-serif;font-weight:700;font-size:20px}
  .prize-five{top:592px;color:var(--pine);font-family:"Barlow Condensed",sans-serif;font-weight:700;font-size:27px}
  .pickup{top:620px;font-size:16px;color:var(--ink)}
  .contact{top:668px;font-family:"Open Sans",sans-serif;font-weight:700;font-size:14.5px;color:var(--ink)}
  .footer-band{position:absolute;left:0;top:715px;width:616px;height:82px;background:var(--berry)}
  .phone-pill{position:absolute;left:174px;top:693px;width:268px;height:44px;border-radius:22px;background:linear-gradient(#2a9a45,var(--pine-dark));color:#fff;display:flex;align-items:center;justify-content:center;gap:12px;font-family:"Barlow Condensed",sans-serif;font-weight:600;font-size:36px}
  .disclaimer{top:747px;color:#fff;font-family:"Open Sans",sans-serif;font-weight:700;font-size:12px;line-height:16px}
  .sponsor-tag{position:absolute;left:230px;top:787px;width:157px;height:22px;border-radius:11px;background:var(--pine);color:#fff;font-family:"Barlow Condensed",sans-serif;font-weight:700;font-size:15px;display:flex;align-items:center;justify-content:center}
  .sponsors{position:absolute;left:36px;right:36px;top:820px;display:flex;justify-content:space-between;align-items:center;height:26px}
  .sponsor{width:30px;height:20px;border-radius:4px;background:#c9a24a}
  .sponsor.round{width:24px;height:24px;border-radius:50%}
</style>
</head>
<body>
<main class="flyer">
  <svg class="flyer-art" viewBox="0 0 616 870">
    <defs>
      <linearGradient id="photoTone" x1="0" y1="0" x2="0" y2="1">
        <stop offset="0" stop-color="#6b625c"/>
        <stop offset=".55" stop-color="#5a3a35"/>
        <stop offset="1" stop-color="#3a2a28"/>
      </linearGradient>
      <linearGradient id="frost" x1="0" y1="0" x2="0" y2="1">
        <stop offset="0" stop-color="#dbe9f3"/>
        <stop offset="1" stop-color="#f4f8fb"/>
      </linearGradient>
    </defs>
    <rect x="0" y="380" width="616" height="335" fill="url(#frost)"/>
    <path role="img" aria-label="Photo of three shoppers in holiday hats and plaid scarves holding wrapped gifts and coffee cups" d="M0 78 Q308 170 616 78 L616 385 Q308 440 0 385 Z" fill="url(#photoTone)"/>
    <path d="M0 48 Q308 160 616 48 L616 80 Q308 150 0 80 Z" fill="var(--pine)"/>
    <path d="M0 372 Q308 424 616 372 L616 392 Q308 444 0 392 Z" fill="var(--pine)"/>
    <path d="M0 386 Q308 440 616 386 L616 400 Q308 452 0 400 Z" fill="#ffffff"/>
    <rect x="41" y="532" width="534" height="1.5" fill="var(--berry)"/>
    <rect x="41" y="574" width="534" height="1.5" fill="var(--berry)"/>
    <rect x="255" y="656" width="106" height="1.5" fill="#2a9a45"/>
  </svg>

  <div class="brand-host">Midtown Harlanby</div>
  <div class="brand-partner"><span class="dot"></span><span>Corner Trader<br>Festday</span></div>

  <div class="line title-script">Browse Every Counter</div>
  <div class="line title-place">MIDTOWN HARLANBY</div>

  <div class="date-pill">NOVEMBER 27, 2021 10:00 A.M. - 2:00 P.M</div>

  <div class="line prize-main">ENTER TO WIN $500</div>
  <div class="line prize-sub">in Shopping Dollars and other gift giveaways!</div>

  <div class="line santa">GET YOUR PICTURES WITH HARLANBY'S HOLIDAY HOST</div>

  <div class="line prize-five">ENTER TO WIN ONE OF FIVE $250 SHOPPING DOLLARS!</div>
  <div class="line pickup">Pick up your FREE Tote &amp; Passport at the Depot</div>

  <div class="line contact">FOR MORE INFORMATION, CONTACT DELLA PRENTISS,</div>

  <div class="footer-band"></div>
  <div class="phone-pill">
    <svg width="26" height="26" viewBox="0 0 24 24" aria-hidden="true"><path fill="#fff" d="M6.6 10.8a15.1 15.1 0 0 0 6.6 6.6l2.2-2.2c.3-.3.7-.4 1-.2 1.1.4 2.3.6 3.6.6.6 0 1 .4 1 1V20c0 .6-.4 1-1 1A17 17 0 0 1 3 4c0-.6.4-1 1-1h3.5c.6 0 1 .4 1 1 0 1.3.2 2.5.6 3.6.1.3 0 .7-.2 1z"/></svg>
    <span>555-014-2290</span>
  </div>
  <div class="line disclaimer">*ELIGIBLE TO BE ENTERED TO WIN WHEN STAMPS FROM ALL PARTICIPATING STORES<br>REFLECTED ON BROWSE EVERY COUNTER PASSPORT</div>

  <div class="sponsor-tag">SPONSORED BY:</div>
  <div class="sponsors" aria-label="Sponsor badges">
    <span class="sponsor" style="background:#b8862e"></span>
    <span class="sponsor round" style="background:#d94040"></span>
    <span class="sponsor" style="background:#e7b9b4"></span>
    <span class="sponsor round" style="background:#6aa3c8"></span>
    <span class="sponsor" style="background:#555"></span>
    <span class="sponsor" style="background:#2f5fa5"></span>
    <span class="sponsor round" style="background:#8a6a4a"></span>
    <span class="sponsor" style="background:#1f3d7a"></span>
    <span class="sponsor round" style="background:#e2c021"></span>
    <span class="sponsor round" style="background:#c94a4a"></span>
  </div>
</main>
</body>
</html>
```